Carpentry and Building Business Card

I'm looking for a business card that is minimalistic and that incorporates the theme of my Velmor logo.
On one side I'd like the VELMOR logo with my details on the other side.
Double sided with curved edges

Target Market(s)

Construction / renovation
Adults

Industry/Entity Type

Tradesman

Contact Information for Business Card

Logo on one side, details on the other

Colors

Designer to choose only greyscale colors for use in the design.

Requirements
Must have
• Nilo Petrakis
VELMOR CONSTRUCT
Carpentry & Building Services
0481236574
Velmorconstruct@brixmail.com
Lic No. 718263D
Nice to have
• Fb and insta icons. @velmorconstruct
Should not have
• No hammer or tool icons please.

No address line.

```html
<!DOCTYPE html>
<html lang="en">
<head>
<meta charset="utf-8">
<title>Velmor Construct – Business Card</title>
<link rel="stylesheet" href="https://fonts.googleapis.com/css2?family=Montserrat:wght@400;500;600&family=Work+Sans:wght@400;500&display=swap">
<style>
  :root {
    --bg: #161616;
    --card: #232222;
    --pattern-light: #3a3a3a;
    --pattern-dark: #1f1f1f;
    --white: #f4f4f4;
    --accent: #f0982f;
  }
  * { box-sizing: border-box; margin: 0; padding: 0; }
  html, body { width: 1200px; height: 900px; overflow: hidden; background: var(--bg); }
  .canvas {
    position: relative; width: 1200px; height: 900px;
    background: radial-gradient(ellipse at 60% 20%, #2e2e2e 0%, var(--bg) 70%);
  }
  .card {
    position: absolute; left: 280px; width: 640px; height: 366px;
    border-radius: 22px; background: var(--card); overflow: hidden;
    box-shadow: 0 14px 30px rgba(0,0,0,0.55);
  }
  .card--back { top: 52px; }
  .card--front { top: 482px; }

  .brand-pattern {
    position: absolute; inset: 0;
    background: linear-gradient(120deg, var(--pattern-light) 0%, #2a2a2a 45%, var(--pattern-dark) 100%);
  }
  .back-title {
    position: absolute; left: 0; right: 0; top: 150px; text-align: center;
    font-family: "Montserrat", sans-serif; color: var(--white);
  }
  .back-title__name { font-size: 27px; font-weight: 500; letter-spacing: 5px; }
  .back-title__tagline { font-family: "Work Sans", sans-serif; font-size: 15px; letter-spacing: 3px; margin-top: 2px; }

  .front-logo {
    position: absolute; left: 46px; top: 124px; display: flex; align-items: center; gap: 14px;
  }
  .front-logo__mark { width: 44px; height: 44px; border: 2px solid var(--accent); flex: none; }
  .front-logo__name {
    font-family: "Montserrat", sans-serif; font-weight: 500; font-size: 28px;
    letter-spacing: 8px; color: var(--white); white-space: nowrap;
  }
  .divider { position: absolute; left: 334px; top: 102px; width: 2px; height: 110px; background: var(--accent); }
  .person { position: absolute; left: 356px; top: 110px; width: 244px; font-family: "Work Sans", sans-serif; color: var(--white); }
  .person__name {
    font-family: "Montserrat", sans-serif; font-weight: 600; font-size: 22px;
    letter-spacing: 2px; color: var(--accent); text-transform: uppercase; white-space: nowrap;
  }
  .person__role { font-size: 15px; margin-top: 2px; letter-spacing: 1px; }
  .contact { list-style: none; margin-top: 14px; font-size: 14px; letter-spacing: 0.4px; }
  .contact li { display: flex; align-items: center; gap: 6px; margin-bottom: 4px; white-space: nowrap; }
  .contact svg { width: 12px; height: 12px; flex: none; }
  .licence {
    position: absolute; left: 46px; top: 290px; font-family: "Work Sans", sans-serif;
    font-size: 15px; color: var(--white); letter-spacing: 1px;
  }
  .rule { position: absolute; left: 200px; top: 302px; width: 314px; height: 1.5px; background: var(--accent); }
  .social { position: absolute; left: 526px; top: 288px; display: flex; gap: 12px; }
  .social__item { width: 28px; height: 28px; border-radius: 5px; background: var(--accent); }
</style>
</head>
<body>
<main class="canvas">
  <section class="card card--back">
    <div class="brand-pattern" role="img" aria-label="Repeating pattern of the Velmor brand symbol in grey outlines"></div>
    <div class="back-title">
      <p class="back-title__name">VELMOR CONSTRUCT</p>
      <p class="back-title__tagline">Carpentry &amp; Building Services</p>
    </div>
  </section>

  <section class="card card--front">
    <div class="front-logo">
      <span class="front-logo__mark"></span>
      <span class="front-logo__name">VELMOR.</span>
    </div>
    <span class="divider"></span>
    <div class="person">
      <p class="person__name">Nilo Petrakis</p>
      <p class="person__role">Director</p>
      <ul class="contact">
        <li>
          <svg viewBox="0 0 12 12" aria-hidden="true"><path d="M3 1 L5 3.5 L4 5 Q5.5 7 7 8 L8.5 7 L11 9 L9.5 11 Q5 10.5 1 3 Z" fill="var(--accent)"/></svg>
          0481236574
        </li>
        <li>
          <svg viewBox="0 0 12 12" aria-hidden="true"><rect x="0.75" y="2.5" width="10.5" height="7" fill="none" stroke="var(--accent)" stroke-width="1.2"/><path d="M1 3 L6 7 L11 3" fill="none" stroke="var(--accent)" stroke-width="1.2"/></svg>
          Velmorconstruct@brixmail.com
        </li>
      </ul>
    </div>
    <p class="licence">Lic No. 718263D</p>
    <span class="rule"></span>
    <div class="social" aria-label="Social profiles @velmorconstruct">
      <span class="social__item"></span>
      <span class="social__item"></span>
    </div>
  </section>
</main>
</body>
</html>
```